Masonry company / pouring concrete / decorative concrete recherche Flyer

We need a Flyer creation to advertise our company called "Ridgeline Concrete". We are a company specializing in decorative concrete / decorative concrete for outdoor landscaping (terraces, patio, driveway etc ...) We want a Flyer size A5 (21cm / 14.8cm) Recto-Verso. Which attracts the eye and especially that shows the different products that we offer (printed concrete / miccrochape / washed concrete / masonry / luminescent concrete / sanitation / earthwork) Our Logo should be recalled and the Flyer must be in the same colors as the logo (white and / or black) and with the same design as the logo (squares).

Target Market(s)

25-80 years

Industry/Entity Type

Concrete

Colors
f78f20
000000
ffffff
9d9d9d

Requirements
Must have
• Logo / photos (even other than those proposed but still on printed concrete) / double-sided /
Nice to have
• It would be nice if the way the flyer is designed, reminds the shape of the logo. For example that the images are arranged like the small squares and rectangles of the logo. It would be nice to have the motif "wood" in the background of the flyer.
Should not have
• You can use the "nameless" file but do not copy it.

```html
<!DOCTYPE html>
<html lang="en">
<head>
<meta charset="utf-8">
<title>Ridgeline Concrete – Flyer</title>
<link rel="stylesheet" href="https://fonts.googleapis.com/css2?family=Anton&family=Oswald:wght@400;500;600;700&family=Montserrat:wght@500&display=swap">
<style>
  :root {
    --orange: #f78f20;
    --black: #000000;
    --white: #ffffff;
    --gray: #9d9d9d;
    --gray-dark: #7f7f7f;
    --wood-light: #e3dcd3;
    --wood-mid: #d5ccc1;
    --stage: #fcebc8;
  }
  * { box-sizing: border-box; margin: 0; padding: 0; }
  html, body { width: 1200px; height: 857px; overflow: hidden; }
  body {
    background: linear-gradient(160deg, #fdf3de 0%, var(--stage) 100%);
    position: relative;
    font-family: "Oswald", sans-serif;
  }
  .page {
    position: absolute;
    top: 61px;
    width: 520px;
    height: 735px;
    overflow: hidden;
    background:
      repeating-linear-gradient(90deg, rgba(255,255,255,0.18) 0 3px, transparent 3px 19px),
      linear-gradient(90deg, var(--wood-light), var(--wood-mid) 45%, var(--wood-light));
    box-shadow: 0 10px 24px rgba(120, 90, 40, 0.25);
  }
  .page--front { left: 60px; }
  .page--back { left: 620px; }

  .bar { position: absolute; background: var(--orange); }

  /* Front */
  .brand-box {
    position: absolute; left: 255px; top: 0; width: 265px; height: 175px;
    background: var(--black);
    border-left: 10px solid var(--orange);
    border-bottom: 10px solid var(--orange);
    display: flex; align-items: center; justify-content: center; gap: 12px;
  }
  .brand-square { width: 26px; height: 26px; background: var(--orange); }
  .brand-name {
    font-family: "Montserrat", sans-serif; font-weight: 500;
    color: var(--orange); font-size: 23px; line-height: 1.15;
  }
  .headline {
    position: absolute; left: 28px; top: 230px; width: 470px;
    font-family: "Anton", sans-serif; color: var(--orange);
    font-size: 58px; line-height: 1.02; text-transform: uppercase;
    text-shadow: -2px -2px 0 var(--black), 2px -2px 0 var(--black), -2px 2px 0 var(--black), 2px 2px 0 var(--black);
  }
  .headline small { font-size: 32px; }
  .tagline {
    position: absolute; left: 28px; top: 365px; width: 480px;
    font-weight: 600; font-size: 18.5px; color: var(--black);
  }
  .services-title {
    position: absolute; left: 0; right: 0; top: 405px; text-align: center;
    font-weight: 700; font-size: 30px; color: var(--black);
  }
  .services-box {
    position: absolute; left: 50px; top: 458px; width: 420px; height: 190px;
    background: var(--gray-dark);
    display: flex; flex-direction: column; justify-content: center; align-items: center;
    color: var(--white); font-weight: 400; font-size: 23px; line-height: 1.25;
  }
  .contact {
    position: absolute; left: 0; right: 0; top: 666px; text-align: center; color: var(--black);
  }
  .contact-label { font-size: 15px; font-weight: 500; }
  .contact-email { font-size: 23px; font-weight: 500; }

  /* Back */
  .photo { position: absolute; }
  .photo--gray { border: 7px solid var(--gray-dark); }
  .photo--orange { border: 7px solid var(--orange); }
  .tab { position: absolute; width: 14px; height: 14px; }
  .tab--orange { background: var(--orange); }
  .tab--gray { background: var(--gray); width: 34px; height: 34px; }
</style>
</head>
<body>

<section class="page page--front" aria-label="Flyer front">
  <div class="bar" style="left:0;top:70px;width:155px;height:24px"></div>
  <div class="bar" style="left:0;top:70px;width:24px;height:185px"></div>

  <div class="brand-box">
    <span class="brand-square"></span>
    <span class="brand-name">Ridgeline<br>Concrete</span>
  </div>

  <h1 class="headline"><small>A</small> Wide Choice <small>of</small><br>Motifs <small>and</small> Colors</h1>
  <p class="tagline">Don't wait to order your printed concrete terrace</p>

  <h2 class="services-title">Our Services</h2>
  <div class="services-box">
    <span>printed concrete / miccrochape</span>
    <span>washed concrete / masonry</span>
    <span>luminescent concrete</span>
    <span>sanitation / earthwork</span>
  </div>

  <div class="bar" style="right:0;top:470px;width:24px;height:190px"></div>
  <div class="bar" style="left:395px;top:636px;width:125px;height:24px"></div>
  <div class="bar" style="left:0;bottom:0;width:32px;height:32px"></div>

  <div class="contact">
    <p class="contact-label">Send your email to</p>
    <p class="contact-email">hello@ridgelineconcrete.com</p>
  </div>
</section>

<section class="page page--back" aria-label="Flyer back">
  <div class="bar" style="left:0;top:95px;width:160px;height:26px"></div>
  <div class="bar" style="left:0;top:95px;width:26px;height:190px"></div>
  <div class="bar" style="right:0;top:420px;width:26px;height:210px"></div>
  <div class="bar" style="left:395px;top:604px;width:125px;height:26px"></div>

  <div class="photo photo--gray" role="img" aria-label="Photo of a printed concrete garden path between trees"
       style="left:330px;top:22px;width:170px;height:112px;background:linear-gradient(180deg,#4f6a3a 0%,#6f7f55 45%,#c9b9a3 70%,#d8c8b2 100%)"></div>
  <div class="tab tab--orange" style="left:484px;top:22px"></div>
  <div class="tab tab--orange" style="left:330px;top:120px"></div>

  <div class="photo photo--gray" role="img" aria-label="Photo of a stamped concrete driveway in front of a modern house"
       style="left:70px;top:88px;width:262px;height:152px;background:linear-gradient(180deg,#c9ccd0 0%,#e8e8e8 35%,#555 55%,#6b6b6b 100%)"></div>

  <div class="photo photo--orange" role="img" aria-label="Photo of a garage interior with a glossy red resin floor"
       style="left:150px;top:245px;width:300px;height:272px;background:linear-gradient(180deg,#d8d4cc 0%,#a7a7a2 40%,#5a5553 60%,#8e1f27 80%,#6f1119 100%)"></div>
  <div class="tab tab--gray" style="left:157px;top:252px"></div>
  <div class="tab tab--gray" style="left:409px;top:476px"></div>

  <div class="photo photo--gray" role="img" aria-label="Photo of concrete colour sample swatches with a red spray gun"
       style="left:292px;top:500px;width:220px;height:150px;background:linear-gradient(135deg,#e9e4df 0%,#cdb59c 40%,#b07f66 60%,#6f8d9a 85%,#2b5d7a 100%)"></div>

  <div class="photo photo--gray" role="img" aria-label="Photo of a dark luminescent concrete surface at night"
       style="left:60px;top:590px;width:170px;height:125px;background:linear-gradient(180deg,#0a0a0a,#1a1a1a)"></div>
  <div class="tab tab--orange" style="left:209px;top:597px"></div>
  <div class="tab tab--orange" style="left:67px;top:694px"></div>
</section>

</body>
</html>
```